Label for a Hair oil product

Label Info:

Dimensions same for label & the mono cartoon design:
Thickness 4.5cm
Height 17.5 cm
Breadth 6.5 cm

Label:

Front:
Brand Name:
English: Velvet Crowne
Arabic: كالنجمة
Oil Name:
English: Velvet Crowne Hair Oil
Arabic: زيت كالنجمة للشعر
Marketing statement:
"لأن الشعر تاج رأس المرأة، من تلبس هذا التاج – في عرف الجمال- تدعى أميرة" – سلمى العتيبي

Velvet Crowne Hair Oil is the founder's secret hair recipe. Our product is based on“hair oil-hair growth” theory that was verified by the founder's personal experience . It is personally tested to prove that it shows amazing results on the hair. It thickens, lengthens and adds shine to your hair only by using natural herbal extracts.

"This recipe worked for me and I decided to share my secret with you"- The Founder.

Back:

Ingredients: - copy from the attached image but for the last statement do not write in coconut oil instead write" in our special blend of herbal oils that will give you the desired hair growth results".

Directions of Use ( For External Use Only):
Apply the oil gently to cover your hair starting 2 cm away from the scalp towards the end of your hair. I highly recommend using our heated gel cap. The heat systematically allows ingredients to penetrate the hair follicles more efficiently for great results. Apply the oil consistently once a week to see the desired results in 4-6 weeks depending on you hair type.

pls add this statement clearly after DOU:
Dear customer you are kindly requested to do a patch test of this product before use to avoid any sensitives you might have against any of our ingredients. Apply a slight amount on any small corner of your hair. Leave it for two hours then rinse with water and shampoo. Wait for 96 hours to roll out any sensitivity.

My Logo is attached. it should be on the top ( front label)

sticker label examples are attached
NOTE:
***the winner will also design the mono cartoon
*** English is my second language so if notice something needs to be corrected pls do and let me know.

Target Market(s)

Girls

Industry/Entity Type

Hair

Font styles to use
Script

Colors
e667a6
b768aa
e34298
eea4c8
f9d9e8
eddcec
ffffff

Requirements
Nice to have
• pictures of Amla or Bhringaraj

```html
<!DOCTYPE html>
<html lang="en">
<head>
<meta charset="utf-8">
<title>Velvet Crowne Hair Oil – Back Label</title>
<link rel="stylesheet" href="https://fonts.googleapis.com/css2?family=Open+Sans:wght@400;600;700&family=Noto+Serif:wght@400;700&family=Courier+Prime&display=swap">
<style>
  :root{
    --frame:#b55ba7;
    --brand:#c2469c;
    --pink-accent:#e34298;
    --alert:#c41e45;
    --ink:#111111;
    --white:#ffffff;
  }
  *{box-sizing:border-box;}
  html,body{margin:0;padding:0;width:1200px;height:3235px;overflow:hidden;background:var(--white);}
  h2,p,dl,dd,address{margin:0;}
  .label{
    position:relative;width:371px;height:1000px;
    transform:scale(3.2345);transform-origin:0 0;
    font-family:"Open Sans",Arial,sans-serif;color:var(--ink);
  }
  .label-shape{position:absolute;inset:0;width:371px;height:1000px;}
  .brand{
    position:absolute;top:72px;left:0;width:371px;text-align:center;
    font-weight:700;font-size:30px;line-height:36px;color:var(--brand);
  }
  .category{position:absolute;top:151px;left:0;width:371px;text-align:center;font-weight:700;font-size:12.8px;line-height:17px;white-space:nowrap;}
  .ingredients-title{position:absolute;top:169px;left:0;width:371px;text-align:center;font-family:"Noto Serif",Georgia,serif;font-weight:700;font-size:13px;line-height:17px;color:var(--pink-accent);}
  .composition{
    position:absolute;top:188px;left:45px;width:285px;
    font-family:"Noto Serif",Georgia,serif;font-size:14px;line-height:18px;
  }
  .composition-head{letter-spacing:1.3px;border-bottom:1px solid var(--ink);padding-bottom:1px;margin-bottom:2px;white-space:nowrap;}
  .ingredient{display:flex;justify-content:space-between;}
  .blend-note{font-size:14.4px;text-align:justify;}
  .rule{position:absolute;top:347px;left:45px;width:285px;border-top:2px solid var(--ink);}
  .directions-title{
    position:absolute;top:357px;left:45px;width:285px;height:27px;
    border:1px solid var(--ink);text-align:center;font-weight:700;font-size:16px;line-height:25px;
  }
  .directions{
    position:absolute;top:393px;left:45px;width:285px;
    font-size:13.3px;line-height:17.6px;text-align:justify;
  }
  .patch-test{
    position:absolute;top:597px;left:40px;width:287px;height:207px;padding:5px 10px;
    border:1.5px solid var(--alert);border-radius:12px;
    color:var(--alert);font-size:14px;line-height:17.6px;text-align:justify;text-align-last:center;
  }
  .batch{
    position:absolute;top:815px;left:45px;width:285px;height:57px;background:var(--white);
    font-size:11px;
  }
  .batch-row{position:absolute;left:8px;display:flex;white-space:nowrap;line-height:15px;}
  .batch-row dt{width:42px;font-family:"Noto Serif",Georgia,serif;font-weight:700;}
  .batch-row .sep{width:48px;font-weight:700;}
  .batch-row dd{font-family:"Courier Prime","Courier New",monospace;font-size:11.5px;}
  .maker-label{position:absolute;top:881px;left:50px;font-family:"Noto Serif",Georgia,serif;font-weight:700;font-size:10.5px;line-height:14px;white-space:nowrap;}
  .maker-name{position:absolute;top:880px;left:0;width:371px;text-align:center;font-weight:700;font-size:12px;line-height:16px;padding-left:30px;}
  .maker-address{position:absolute;top:897px;left:0;width:371px;text-align:center;font-size:12.5px;line-height:17px;font-style:normal;}
  .volume{position:absolute;top:933px;right:27px;font-weight:700;font-size:22px;line-height:28px;}
</style>
</head>
<body>
<main class="label">
  <svg class="label-shape" viewBox="0 0 371 1000" aria-hidden="true">
    <defs>
      <linearGradient id="panelFill" x1="0" y1="0" x2="0" y2="1">
        <stop offset="0" stop-color="#ffffff"/>
        <stop offset="0.32" stop-color="#ffffff"/>
        <stop offset="0.6" stop-color="#f7e3ee"/>
        <stop offset="1" stop-color="#efc3dc"/>
      </linearGradient>
    </defs>
    <path d="M0 1000 V185.5 A185.5 185.5 0 0 1 371 185.5 V1000 Z" fill="var(--frame)"/>
    <path d="M17 990 V185.5 A168.5 168.5 0 0 1 354 185.5 V990 Z" fill="url(#panelFill)"/>
  </svg>

  <div class="brand">Velvet Crowne</div>

  <div class="category">An Ayurvedic Proprietary Medicine</div>
  <div class="ingredients-title">Keys Ingredients</div>

  <section class="composition">
    <div class="composition-head">Each ml contains extract of :</div>
    <div class="ingredient"><span>Amla</span><span>0.1ml</span></div>
    <div class="ingredient"><span>Bhringaraj</span><span>0.1ml</span></div>
    <div class="ingredient"><span>Brahmi</span><span>0.1ml</span></div>
    <p class="blend-note">Prepared with extracts of Asparagus Jatamansi Hibiscus in a special blend of oils that will give you the desired hair growth results .</p>
  </section>
  <div class="rule"></div>

  <h2 class="directions-title">Directions of Use</h2>
  <p class="directions">(For External Use Only): Apply the oil gently to cover your hair starting 2 cm away from the scalp towards the end of your hair. I highly recommend using a heated gel cap. The heat systematically allows ingredients to penetrate the hair follicles more efficiently for great results. Apply the oil consistently once a week to see the desired results in 4-6 weeks depending on you hair type.</p>

  <p class="patch-test">Dear customer you are kindly requested to do a patch test of this product before use to avoid any sensitives you might have against any of our ingredients. Apply a slight amount on any small corner of your hair. Leave it for two hours then rinse with water and shampoo.<br>Wait for 96 hours to roll out any sensitivity.</p>

  <dl class="batch">
    <div class="batch-row" style="top:5px"><dt>B.NO</dt><span class="sep">:</span><dd>&nbsp;&nbsp;&nbsp;&nbsp;75</dd></div>
    <div class="batch-row" style="top:22px"><dt>MFD</dt><span class="sep">:</span><dd>FEB 2018</dd></div>
    <div class="batch-row" style="top:39px"><dt>EXP Dt</dt><span class="sep">:</span><dd>JAN 2021</dd></div>
  </dl>

  <div class="maker-label">Mfd.By :</div>
  <div class="maker-name">LUMEN HERBALS</div>
  <address class="maker-address">12, Rosewood Garden Lane<br>Meadowbrook, Greenfield - 400 210, India</address>
  <div class="volume">200 ml</div>
</main>
</body>
</html>
```